DRIFTING PAST LANTERNS - A QUIET HARBOUR

A5 size book of 190 - 210 (70 or 80 gsm wood free paper). The concept revolves around an unseen being that stands on a lotus flower who enters an Indian temple with many of his devotees. Traditional design with photography of a colourful Indian temple is preferred though alternative idea would also be considered. Short narratives at the back of book would give prospective readers an instantaneous insight into the story.

```html
<!DOCTYPE html>
<html lang="en">
<head>
<meta charset="utf-8">
<title>Drifting Past Lanterns – Cover</title>
<link rel="stylesheet" href="https://fonts.googleapis.com/css2?family=Satisfy&family=Dancing+Script:wght@500&family=Kaushan+Script&family=Roboto+Condensed:wght@400&display=swap">
<style>
  :root {
    --night-deep: #0b1020;
    --night-blue: #1c2850;
    --wall-blue: #2a3866;
    --stone-light: #b9b3a2;
    --stone-mid: #7d7b78;
    --stone-shade: #3f4560;
    --glow-gold: #f6c04a;
    --glow-amber: #e58e2c;
    --haze-violet: #8a6d92;
    --title-white: #ffffff;
    --rule-white: rgba(255,255,255,0.85);
    --author-orange: #f28a1c;
  }
  * { margin: 0; padding: 0; box-sizing: border-box; }
  html, body {
    width: 1086px;
    height: 1200px;
    overflow: hidden;
    background: var(--night-deep);
  }
  .cover {
    position: relative;
    width: 1086px;
    height: 1200px;
    overflow: hidden;
  }
  .cover-art {
    position: absolute;
    inset: 0;
    width: 1086px;
    height: 1200px;
    display: block;
  }
  .cover-text {
    position: absolute;
    left: 0;
    right: 0;
    top: 946px;
    display: flex;
    flex-direction: column;
    align-items: center;
  }
  .book-title {
    font-family: "Satisfy", "Dancing Script", cursive;
    font-weight: 400;
    font-size: 72px;
    line-height: 1;
    color: var(--title-white);
    text-shadow: 0 2px 8px rgba(0,0,0,0.7);
    white-space: nowrap;
  }
  .book-subtitle {
    margin-top: 24px;
    display: flex;
    align-items: center;
    gap: 16px;
  }
  .book-subtitle .rule {
    width: 112px;
    height: 1px;
    background: var(--rule-white);
  }
  .book-subtitle .label {
    font-family: "Roboto Condensed", sans-serif;
    font-size: 26px;
    color: var(--title-white);
    white-space: nowrap;
  }
  .book-author {
    margin-top: 22px;
    font-family: "Kaushan Script", cursive;
    font-size: 44px;
    line-height: 1;
    color: var(--author-orange);
  }
</style>
</head>
<body>
  <main class="cover">
    <svg class="cover-art" viewBox="0 0 1086 1200" role="img" aria-label="Photographic scene: a weathered stone archway at night framing a golden sunlit Indian temple beneath a glowing tree, with a dark silhouetted figure standing on a pink lotus flower and petals scattered on the ground">
      <defs>
        <radialGradient id="wall-glow" cx="0.5" cy="0.42" r="0.7">
          <stop offset="0" stop-color="var(--wall-blue)"/>
          <stop offset="0.6" stop-color="var(--night-blue)"/>
          <stop offset="1" stop-color="var(--night-deep)"/>
        </radialGradient>
        <linearGradient id="stone-band" x1="0" y1="0" x2="0" y2="1">
          <stop offset="0" stop-color="var(--stone-light)"/>
          <stop offset="0.55" stop-color="var(--stone-mid)"/>
          <stop offset="1" stop-color="var(--stone-shade)"/>
        </linearGradient>
        <radialGradient id="opening-light" cx="0.5" cy="0.6" r="0.6">
          <stop offset="0" stop-color="var(--glow-gold)"/>
          <stop offset="0.45" stop-color="var(--glow-amber)"/>
          <stop offset="0.85" stop-color="var(--haze-violet)"/>
          <stop offset="1" stop-color="#5d5a86"/>
        </radialGradient>
        <linearGradient id="floor-fade" x1="0" y1="0" x2="0" y2="1">
          <stop offset="0" stop-color="var(--night-deep)" stop-opacity="0"/>
          <stop offset="0.45" stop-color="var(--night-deep)" stop-opacity="0.85"/>
          <stop offset="1" stop-color="var(--night-deep)"/>
        </linearGradient>
      </defs>
      <rect class="wall" width="1086" height="1200" fill="url(#wall-glow)"/>
      <path class="arch-band" d="M176 960 L176 440 L224 440 Q250 210 543 30 Q836 210 862 440 L910 440 L910 960 Z" fill="url(#stone-band)" opacity="0.85"/>
      <rect class="pier pier-left" x="136" y="428" width="128" height="540" fill="var(--stone-shade)" opacity="0.9"/>
      <rect class="pier pier-right" x="810" y="428" width="134" height="540" fill="var(--stone-shade)" opacity="0.9"/>
      <rect class="capital capital-left" x="132" y="424" width="136" height="52" fill="var(--stone-mid)"/>
      <rect class="capital capital-right" x="806" y="424" width="142" height="52" fill="var(--stone-mid)"/>
      <path class="arch-opening" d="M264 960 L264 470 Q290 285 543 160 Q796 285 822 470 L822 960 Z" fill="url(#opening-light)"/>
      <rect class="floor" x="0" y="820" width="1086" height="380" fill="url(#floor-fade)"/>
    </svg>
    <div class="cover-text">
      <h1 class="book-title">Drifting Past Lanterns</h1>
      <p class="book-subtitle">
        <span class="rule"></span>
        <span class="label">A Quiet Harbour</span>
        <span class="rule"></span>
      </p>
      <p class="book-author">Mirelo</p>
    </div>
  </main>
</body>
</html>
```